App Redesign for PathMentor

We're looking for a skilled UI/UX designer to modernize the PathMentor mobile app, enhancing user engagement while preserving our current brand identity.

Key Objectives:
Refresh the app using modern design trends
Maintain a clean, calm, and playful aesthetic aligned with our brand
Boost engagement through improved flow, visuals, and interactivity

Design Requirements:
Retain recognizability from our app and website (see Brand ID Guide) (and website pathmentorhub.example)
Reflect a tone that is supportive, fun/ playful, and professional

Design 5–8 key screens, including:
Home/Dashboard
Daily Intentions Interface
Gamification Overview (Streaks, Rewards)
Social Features (Direct Realtime Feedback, Messaging, Challenges)
Progress Tracking

New Feature Concepts to Include:
Daily Intentions with voice/text input and visual encouragement
Gamification elements like streaks, badges, and animations
Social Connections including messaging, reactions, and feedback tools
Optional: Subtle design cues for future AI-driven interactions

Audience: Adults aged 25–55 interested in personal development and coaching. Tech-comfortable but not tech-savvy.

Visual Inspiration: Lexaroo (gamification), Calmnook (intentions), Pacely (social support)

Target Market(s)

Corporate Leaders and Entrepreneurs

Industry/Entity Type

Leadership Training & Consultancies

Font styles to use
Sans Serif
Other font styles liked:
• Avenir, Arial

Colors
FFF300
FFF600
FEFA6F
FFFEC7
FFFEE8

Requirements
Nice to have
• Lexaroo, Calmnook,

```html
<!DOCTYPE html>
<html lang="en">
<head>
<meta charset="utf-8">
<title>PathMentor – App Screens</title>
<link rel="stylesheet" href="https://fonts.googleapis.com/css2?family=Nunito+Sans:wght@400;600;700;800&display=swap">
<style>
:root{
  --bg:#E6E6E6;
  --yellow:#FFD600;
  --yellow-deep:#F2C600;
  --brand-text:#F5C200;
  --taupe:#B4ACA7;
  --taupe-dark:#A49C97;
  --cream:#FBF2AA;
  --chip:#FBEFA3;
  --bubble-grey:#EFEAE7;
  --ink:#1E1E1E;
  --muted:#8C8C8C;
  --line:#DADADA;
  --orange:#F9A300;
  --green:#22D46A;
  --white:#FFFFFF;
}
*{box-sizing:border-box;margin:0;padding:0}
html,body{width:1200px;height:715px;overflow:hidden;background:var(--bg)}
body{font-family:"Nunito Sans",Arial,sans-serif;color:var(--ink)}
.board{position:absolute;left:0;top:0;width:2492px;height:1484px;transform:scale(.48154);transform-origin:0 0}
.phone{position:absolute;top:52px;width:333px;background:var(--white);border-radius:30px;overflow:hidden;box-shadow:0 6px 18px rgba(0,0,0,.08)}
.phone-head{position:absolute;left:0;top:0;width:333px;height:102px;background:var(--yellow);border-radius:0 0 60px 60px;overflow:hidden}
.phone-head::after{content:"";position:absolute;right:-20px;top:-30px;width:150px;height:100px;border-radius:50%;border:26px solid var(--yellow-deep);opacity:.7}
.status{position:absolute;left:17px;top:11px;font-size:12px;font-weight:700;z-index:2}
.status-icons{position:absolute;right:16px;top:12px;z-index:2}
.screen-title{position:absolute;left:0;right:0;top:34px;text-align:center;font-size:19px;font-weight:800;z-index:2}
.head-icon{position:absolute;left:156px;top:38px;z-index:2}
.brand-pill{position:absolute;left:37px;top:70px;width:260px;height:58px;background:var(--white);border-radius:30px;box-shadow:0 4px 10px rgba(0,0,0,.12);display:flex;align-items:center;justify-content:center;gap:10px}
.brand-dot{width:22px;height:22px;border-radius:50%;background:var(--yellow)}
.brand-name{font-size:20px;font-weight:700;color:var(--brand-text)}
.abs{position:absolute}
.label{font-size:17px}
.tabbar{position:absolute;left:0;bottom:0;width:333px;height:68px;background:var(--taupe);display:flex;align-items:flex-start;padding-top:18px}
.tab{flex:1;display:flex;flex-direction:column;align-items:center;color:var(--white);font-size:7.5px;line-height:1.1;text-align:center}
.tab svg{width:20px;height:20px;margin-bottom:3px}
.tab.active{margin-top:-38px;font-size:10px;font-weight:600;white-space:nowrap;flex:1.3}
.tab.active .disc{width:54px;height:54px;border-radius:50%;background:var(--yellow);border:5px solid var(--white);display:flex;align-items:center;justify-content:center;margin-bottom:4px;box-shadow:0 2px 6px rgba(0,0,0,.12)}
.tab.active .disc svg{width:24px;height:24px;margin:0}
.card{position:absolute;background:var(--white);border-radius:8px;box-shadow:0 2px 10px rgba(0,0,0,.12)}
.stat{position:absolute;top:183px;width:141px;height:56px;border-radius:4px;padding:6px 13px}
.stat b{font-size:19px;display:block;line-height:1.1}
.stat span{font-size:13px}
.stat svg{position:absolute;right:10px;top:8px}
.stat-weekly{left:16px;background:var(--taupe)}
.stat-monthly{left:173px;background:var(--yellow)}
.chart-title{position:absolute;left:12px;top:12px;right:10px;font-size:10.5px;font-weight:800;color:#444;line-height:1.35}
.greeting{position:absolute;left:43px;top:150px;width:247px;height:62px;background:var(--taupe);border:2px solid var(--yellow);border-radius:10px;color:var(--white);font-weight:700;font-size:13.5px;text-align:center;padding-top:10px;line-height:1.6}
.field{position:absolute;left:16px;width:301px;height:46px;border:1px solid var(--line);border-radius:23px;font-size:13px;color:#555;display:flex;align-items:center;padding:0 17px;justify-content:space-between}
.field.placeholder{color:#aaa;font-size:14px;padding-left:23px}
.chip{position:absolute;top:607px;height:46px;background:var(--chip);border-radius:23px;display:flex;align-items:center;gap:10px;padding:0 14px;font-size:15px;font-weight:600}
.toggle{position:absolute;left:253px;top:716px;width:64px;height:36px;border-radius:18px;background:var(--taupe-dark)}
.toggle::after{content:"";position:absolute;right:4px;top:4px;width:28px;height:28px;border-radius:50%;background:var(--white)}
.bubble{position:absolute;width:193px;height:39px;border-radius:20px;font-size:14px;font-weight:400;display:flex;align-items:center;padding-left:23px}
.bubble.in{left:16px;background:var(--bubble-grey)}
.bubble.out{left:124px;background:var(--chip)}
.composer{position:absolute;left:16px;top:512px;width:254px;height:39px;border-radius:20px;box-shadow:0 1px 6px rgba(0,0,0,.15);display:flex;align-items:center;gap:8px;padding:0 10px;font-size:11px;color:#bbb}
.mic-btn{position:absolute;left:277px;top:512px;width:40px;height:40px;border-radius:50%;background:var(--yellow);display:flex;align-items:center;justify-content:center}
.seg{position:absolute;left:72px;top:153px;width:190px;height:40px;border-radius:20px;background:var(--taupe);display:flex;align-items:center;padding:0 5px;font-size:15px;font-weight:600}
.seg .on{width:95px;height:31px;border-radius:16px;background:var(--yellow);display:flex;align-items:center;justify-content:center}
.seg .off{flex:1;text-align:center;color:var(--white)}
.week-row{position:absolute;left:18px;width:298px;height:40px;border:1px solid var(--line);border-radius:12px;font-size:15px;font-weight:600;display:flex;align-items:center;justify-content:space-between;padding:0 14px 0 20px}
.vcard{position:absolute;left:16px;width:301px;border-radius:10px;border:1px solid var(--line);overflow:hidden;background:var(--white)}
.vcard-head{height:40px;background:var(--taupe);color:var(--white);font-size:15px;font-weight:600;padding:9px 18px}
.entry{position:relative;padding:11px 18px 0;font-size:10.5px;line-height:1.9}
.entry b{font-size:12px;font-weight:700}
.entry .bell{position:absolute;right:14px;top:14px}
.entry + .entry{border-top:1px solid var(--line);margin-top:12px}
.btn-report{display:inline-block;margin:8px 0 0;background:var(--yellow);border-radius:16px;font-size:12px;font-weight:600;padding:6px 16px}
.section{position:absolute;left:16px;font-size:16px;display:flex;gap:5px;align-items:center}
.streak-art{position:absolute;left:10px;top:10px;width:281px;height:108px;border-radius:6px;background:linear-gradient(180deg,#FFFFFF 0%,#EEF6E6 55%,#E9E2DC 100%)}
.badge{position:absolute;left:18px;display:flex;gap:12px;align-items:flex-start}
.badge .medal{width:38px;height:38px;border-radius:50%;background:var(--yellow);display:flex;align-items:center;justify-content:center}
.badge .name{font-size:14px;font-weight:600}
.badge .meta{font-size:12px;color:#444;display:flex;gap:6px;align-items:center}
.badge .meta small{font-size:7.5px;color:var(--muted)}
.badge.faded{opacity:.22}
.xp-row{position:absolute;left:16px;width:301px;height:46px;border:1px solid var(--line);border-radius:12px;font-size:13px;display:flex;align-items:center;justify-content:space-between;padding:0 14px 0 17px}
.level{position:absolute;top:1222px;width:100px;text-align:center;font-size:12.5px;line-height:1.5}
</style>
</head>
<body>
<svg width="0" height="0" style="position:absolute">
  <defs>
    <symbol id="i-home" viewBox="0 0 24 24"><path d="M12 3 2 12h3v8h5v-5h4v5h5v-8h3z" fill="currentColor"/></symbol>
    <symbol id="i-people" viewBox="0 0 24 24"><circle cx="7" cy="7" r="4" fill="currentColor"/><circle cx="17" cy="7" r="4" fill="currentColor"/><rect x="3" y="13" width="8" height="8" rx="3" fill="currentColor"/><path d="M17 21s-5-3-5-6a2.5 2.5 0 0 1 5-1 2.5 2.5 0 0 1 5 1c0 3-5 6-5 6z" fill="currentColor"/></symbol>
    <symbol id="i-target" viewBox="0 0 24 24"><circle cx="12" cy="12" r="9" fill="none" stroke="currentColor" stroke-width="2"/><circle cx="12" cy="12" r="5" fill="none" stroke="currentColor" stroke-width="2"/><circle cx="12" cy="12" r="1.6" fill="currentColor"/><path d="M12 12 20 4M17 3h4v4" stroke="currentColor" stroke-width="2" fill="none"/></symbol>
    <symbol id="i-game" viewBox="0 0 24 24"><path d="M6 8h12a4 4 0 0 1 4 4l-1 6a2 2 0 0 1-3.5 1L15 16H9l-2.5 3A2 2 0 0 1 3 18l-1-6a4 4 0 0 1 4-4z" fill="currentColor"/><path d="M7 11v4M5 13h4" stroke="#fff" stroke-width="1.5"/><circle cx="16" cy="12" r="1" fill="#fff"/><circle cx="18" cy="14" r="1" fill="#fff"/><circle cx="12" cy="5" r="2" fill="currentColor"/></symbol>
    <symbol id="i-clip" viewBox="0 0 24 24"><rect x="5" y="4" width="14" height="17" rx="2" fill="none" stroke="currentColor" stroke-width="2"/><rect x="9" y="2" width="6" height="4" rx="1" fill="currentColor"/><path d="M8 11h8M8 14h8M8 17h5" stroke="currentColor" stroke-width="1.6"/></symbol>
    <symbol id="i-chart" viewBox="0 0 24 24"><rect x="4" y="13" width="3" height="7" fill="currentColor"/><rect x="9" y="9" width="3" height="11" fill="currentColor"/><rect x="14" y="11" width="3" height="9" fill="currentColor"/><path d="M3 11 9 6l4 3 7-6" stroke="currentColor" stroke-width="2" fill="none"/></symbol>
    <symbol id="i-ask" viewBox="0 0 24 24"><path d="M4 4h16v12H9l-5 4z" fill="currentColor"/><text x="12" y="14" text-anchor="middle" font-size="10" font-weight="800" fill="#B4ACA7" font-family="Arial">?</text></symbol>
    <symbol id="i-menu" viewBox="0 0 24 24"><path d="M4 6h16M4 12h16M4 18h16" stroke="currentColor" stroke-width="2.2"/></symbol>
    <symbol id="i-mic" viewBox="0 0 24 24"><rect x="9" y="2" width="6" height="12" rx="3" fill="currentColor"/><path d="M6 11a6 6 0 0 0 12 0M12 17v4M9 21h6" stroke="currentColor" stroke-width="1.8" fill="none"/></symbol>
    <symbol id="i-chev" viewBox="0 0 24 24"><path d="m9 6 6 6-6 6" stroke="currentColor" stroke-width="2.2" fill="none"/></symbol>
    <symbol id="i-bell" viewBox="0 0 24 24"><path d="M12 3a6 6 0 0 0-6 6v5l-2 3h16l-2-3V9a6 6 0 0 0-6-6zM10 19a2 2 0 0 0 4 0z" fill="currentColor"/><circle cx="19" cy="5" r="4" fill="#FFD600"/></symbol>
    <symbol id="i-lock" viewBox="0 0 24 24"><rect x="5" y="10" width="14" height="11" rx="2" fill="currentColor"/><path d="M8 10V7a4 4 0 0 1 8 0v3" stroke="currentColor" stroke-width="2" fill="none"/></symbol>
    <symbol id="i-status" viewBox="0 0 64 12"><rect x="0" y="8" width="2" height="3" fill="#000"/><rect x="3" y="6" width="2" height="5" fill="#000"/><rect x="6" y="3" width="2" height="8" fill="#000"/><rect x="9" y="0" width="2" height="11" fill="#000"/><path d="M22 10l-2.5-3a4 4 0 0 1 5 0zM17 5a8 8 0 0 1 10 0l-1.5 1.5a6 6 0 0 0-7 0z" fill="#000"/><rect x="40" y="1" width="18" height="10" rx="2" fill="none" stroke="#000"/><rect x="42" y="3" width="14" height="6" fill="#000"/><rect x="59" y="4" width="2" height="4" fill="#000"/></symbol>
  </defs>
</svg>

<main class="board">

<!-- Home / Dashboard -->
<section class="phone" style="left:72px;height:1060px">
  <header class="phone-head">
    <span class="status">8:41 Am</span><svg class="status-icons" width="64" height="12"><use href="#i-status"/></svg>
    <svg class="head-icon" width="22" height="22"><use href="#i-home"/></svg>
  </header>
  <div class="brand-pill"><span class="brand-dot"></span><span class="brand-name">PathMentor</span></div>

  <p class="abs label" style="left:15px;top:150px">ClearMind<sub style="font-size:8px">TM</sub> Tracker</p>
  <div class="stat stat-weekly"><b>271</b><span>Weekly Reports</span><svg width="22" height="22"><use href="#i-chart"/></svg></div>
  <div class="stat stat-monthly"><b>75</b><span>Monthly Reports</span><svg width="22" height="22"><use href="#i-clip"/></svg></div>

  <p class="abs label" style="left:15px;top:261px">Your Overall Progress</p>
  <div class="card" style="left:16px;top:294px;width:301px;height:168px">
    <svg width="301" height="168" font-size="10" fill="#999" font-family="Nunito Sans,Arial">
      <g stroke="#EEE"><line x1="38" y1="20" x2="288" y2="20"/><line x1="38" y1="45" x2="288" y2="45"/><line x1="38" y1="68" x2="288" y2="68"/><line x1="38" y1="92" x2="288" y2="92"/><line x1="38" y1="116" x2="288" y2="116"/><line x1="38" y1="140" x2="288" y2="140"/></g>
      <text x="12" y="24">100</text><text x="15" y="49">80</text><text x="15" y="72">60</text><text x="15" y="96">40</text><text x="15" y="120">20</text><text x="15" y="144">10</text>
      <polyline points="45,85 65,78 86,92 106,98 126,103 146,105 166,94 186,101 206,98 226,98 246,102 266,99" fill="none" stroke="#888" stroke-width="1.2"/>
      <g fill="#fff" stroke="var(--yellow)" stroke-width="2"><circle cx="45" cy="85" r="2.5"/><circle cx="65" cy="78" r="2.5"/><circle cx="86" cy="92" r="2.5"/><circle cx="106" cy="98" r="2.5"/><circle cx="126" cy="103" r="2.5"/><circle cx="146" cy="105" r="2.5"/><circle cx="166" cy="94" r="2.5"/><circle cx="186" cy="101" r="2.5"/><circle cx="206" cy="98" r="2.5"/><circle cx="226" cy="98" r="2.5"/><circle cx="246" cy="102" r="2.5"/><circle cx="266" cy="99" r="2.5"/></g>
    </svg>
  </div>

  <p class="abs label" style="left:15px;top:476px">Your Growth</p>
  <div class="card" style="left:16px;top:508px;width:301px;height:206px;overflow:hidden">
    <p class="chart-title">BODY: Did I take a cold shower or swim in the river today?</p>
    <svg class="abs" style="left:0;top:0" width="301" height="206" font-size="7" fill="#bbb" font-family="Nunito Sans,Arial">
      <text x="14" y="66">5.0</text><text x="14" y="87">4.0</text><text x="14" y="108">3.0</text><text x="14" y="129">2.0</text><text x="14" y="150">1.0</text><text x="14" y="168">0</text>
      <line x1="52" y1="64" x2="285" y2="64" stroke="var(--orange)" stroke-width="1"/>
      <g fill="var(--orange)">
        <rect x="60" y="156" width="6" height="10"/><rect x="80" y="156" width="6" height="10"/><rect x="90" y="126" width="6" height="40"/><rect x="110" y="126" width="6" height="40"/><rect x="120" y="126" width="6" height="40"/><rect x="130" y="126" width="6" height="40"/><rect x="160" y="86" width="6" height="80"/><rect x="170" y="126" width="6" height="40"/><rect x="180" y="146" width="6" height="20"/><rect x="200" y="126" width="6" height="40"/><rect x="210" y="126" width="6" height="40"/><rect x="220" y="126" width="6" height="40"/><rect x="230" y="126" width="6" height="40"/><rect x="240" y="146" width="6" height="20"/><rect x="250" y="126" width="6" height="40"/><rect x="260" y="146" width="6" height="20"/><rect x="264" y="106" width="6" height="60"/><rect x="282" y="146" width="6" height="20"/>
      </g>
      <g font-size="6.5">
        <text x="40" y="190" transform="rotate(-45 40 190)">Wk 50</text><text x="62" y="190" transform="rotate(-45 62 190)">Wk 1</text><text x="84" y="190" transform="rotate(-45 84 190)">Wk 3</text><text x="106" y="190" transform="rotate(-45 106 190)">Wk 5</text><text x="128" y="190" transform="rotate(-45 128 190)">Wk 7</text><text x="150" y="190" transform="rotate(-45 150 190)">Wk 9</text><text x="172" y="190" transform="rotate(-45 172 190)">Wk 11</text><text x="194" y="190" transform="rotate(-45 194 190)">Wk 13</text><text x="216" y="190" transform="rotate(-45 216 190)">Wk 15</text><text x="238" y="190" transform="rotate(-45 238 190)">Wk 17</text><text x="260" y="190" transform="rotate(-45 260 190)">Wk 19</text>
      </g>
    </svg>
  </div>

  <div class="card" style="left:16px;top:736px;width:301px;height:206px">
    <p class="chart-title" style="top:20px">BALANCE: what was focus in family activities?</p>
    <svg class="abs" style="left:0;top:0" width="301" height="206" font-size="7" fill="#bbb" font-family="Nunito Sans,Arial">
      <text x="20" y="58">7</text><text x="20" y="86">5</text><text x="20" y="114">3</text><text x="20" y="142">1</text><text x="20" y="158">0</text>
      <g fill="var(--green)">
        <rect x="45" y="72" width="7" height="84"/><rect x="63" y="72" width="7" height="84"/><rect x="81" y="72" width="7" height="84"/><rect x="99" y="72" width="7" height="84"/><rect x="117" y="72" width="7" height="84"/><rect x="135" y="58" width="7" height="98"/><rect x="153" y="72" width="7" height="84"/><rect x="171" y="72" width="7" height="84"/><rect x="189" y="72" width="7" height="84"/><rect x="207" y="72" width="7" height="84"/><rect x="225" y="66" width="7" height="90"/><rect x="243" y="72" width="7" height="84"/><rect x="261" y="58" width="7" height="98"/>
      </g>
      <g fill="var(--orange)">
        <rect x="54" y="72" width="7" height="84"/><rect x="72" y="80" width="7" height="76"/><rect x="90" y="72" width="7" height="84"/><rect x="108" y="72" width="7" height="84"/><rect x="126" y="72" width="7" height="84"/><rect x="144" y="72" width="7" height="84"/><rect x="162" y="72" width="7" height="84"/><rect x="180" y="72" width="7" height="84"/><rect x="198" y="72" width="7" height="84"/><rect x="216" y="72" width="7" height="84"/><rect x="234" y="72" width="7" height="84"/><rect x="252" y="80" width="7" height="76"/><rect x="270" y="72" width="7" height="84"/>
      </g>
      <line x1="40" y1="114" x2="282" y2="114" stroke="#333" stroke-width="1"/>
    </svg>
  </div>

  <nav class="tabbar">
    <div class="tab active"><span class="disc"><svg style="color:#fff"><use href="#i-home"/></svg></span>Home</div>
    <div class="tab"><svg><use href="#i-people"/></svg>Social<br>Features</div>
    <div class="tab"><svg><use href="#i-target"/></svg>Daily<br>Intensions</div>
    <div class="tab"><svg><use href="#i-game"/></svg>Gamification</div>
    <div class="tab"><svg><use href="#i-clip"/></svg>Progress<br>Tracking</div>
  </nav>
</section>

<!-- Daily Intentions -->
<section class="phone" style="left:477px;height:868px">
  <header class="phone-head">
    <span class="status">8:41 Am</span><svg class="status-icons" width="64" height="12"><use href="#i-status"/></svg>
    <h1 class="screen-title">Daily Intentions</h1>
  </header>
  <div class="brand-pill"><span class="brand-dot"></span><span class="brand-name">PathMentor</span></div>

  <div class="greeting">Good morning, Mark Dalen<br>What’s your focus today?</div>
  <p class="abs" style="left:16px;top:236px;font-size:15.5px;line-height:1.65">Take a mindful moment to align your<br>intention with your day</p>
  <div class="field" style="top:298px">What do you want to practice?<svg width="16" height="18" style="color:#666"><use href="#i-mic"/></svg></div>
  <div class="field" style="top:356px">Where will you apply it?<svg width="16" height="18" style="color:#666"><use href="#i-mic"/></svg></div>
  <div class="field" style="top:412px">How will success feel or look?<svg width="16" height="18" style="color:#666"><use href="#i-mic"/></svg></div>
  <p class="abs" style="left:16px;top:474px;font-size:15.5px">Enter intentions?</p>
  <div class="field placeholder" style="top:507px">Type Here<svg width="16" height="18" style="color:#666"><use href="#i-mic"/></svg></div>
  <p class="abs" style="left:16px;top:573px;font-size:15.5px">Past intentions?</p>
  <div class="chip" style="left:16px"><svg width="24" height="22"><use href="#i-people"/></svg>Mediation</div>
  <div class="chip" style="left:156px"><svg width="24" height="22"><use href="#i-game"/></svg>Gym Hitting</div>
  <svg class="abs" style="left:308px;top:620px" width="14" height="14"><use href="#i-chev"/></svg>
  <p class="abs" style="left:16px;top:678px;font-size:15.5px">Set Timer</p>
  <p class="abs" style="left:16px;top:710px;font-size:17px">07:00 <small style="font-size:11px">AM</small></p>
  <p class="abs" style="left:16px;top:739px;font-size:10px;color:#bbb">Wake Up OR Others</p>
  <div class="toggle"></div>

  <nav class="tabbar" style="height:70px">
    <div class="tab"><svg><use href="#i-home"/></svg>Home</div>
    <div class="tab"><svg><use href="#i-people"/></svg>Social<br>Features</div>
    <div class="tab active"><span class="disc"><svg style="color:#fff"><use href="#i-target"/></svg></span>Daily Intentions</div>
    <div class="tab"><svg><use href="#i-game"/></svg>Gamification</div>
    <div class="tab"><svg><use href="#i-clip"/></svg>Progress<br>Tracking</div>
  </nav>
</section>

<!-- Social Features -->
<section class="phone" style="left:881px;height:643px">
  <header class="phone-head">
    <span class="status">8:41 Am</span><svg class="status-icons" width="64" height="12"><use href="#i-status"/></svg>
    <h1 class="screen-title">Social Features</h1>
  </header>
  <div class="brand-pill"><span class="brand-dot"></span><span class="brand-name">PathMentor</span></div>

  <div class="bubble in" style="top:153px">Lorem ipsum dolor s</div>
  <div class="bubble out" style="top:208px">Excepteur sint occaeca</div>
  <div class="bubble in" style="top:265px">Lorem ipsum dolor s</div>
  <div class="bubble out" style="top:320px">Excepteur sint occaeca</div>
  <div class="bubble in" style="top:377px">Lorem ipsum dolor s</div>
  <div class="bubble out" style="top:432px">Excepteur sint occaeca</div>
  <div class="composer">
    <svg width="18" height="18"><circle cx="9" cy="9" r="7.5" fill="none" stroke="#999"/><circle cx="6.5" cy="7.5" r="1" fill="#999"/><circle cx="11.5" cy="7.5" r="1" fill="#999"/><path d="M5.5 10.5a3.5 3.5 0 0 0 7 0" stroke="#999" fill="none"/></svg>
    <span style="flex:1">Type a message</span>
    <svg width="16" height="16"><path d="M11 4 5 10a2 2 0 0 0 3 3l6-6a3.5 3.5 0 0 0-5-5L3 8" stroke="#999" stroke-width="1.4" fill="none"/></svg>
    <svg width="16" height="16"><rect x="1" y="4" width="14" height="10" rx="2" fill="#999"/><circle cx="8" cy="9" r="3" fill="#fff"/></svg>
  </div>
  <div class="mic-btn"><svg width="20" height="22"><use href="#i-mic"/></svg></div>

  <nav class="tabbar">
    <div class="tab"><svg><use href="#i-home"/></svg>Home</div>
    <div class="tab active"><span class="disc"><svg style="color:#fff"><use href="#i-people"/></svg></span>Social Features</div>
    <div class="tab"><svg><use href="#i-target"/></svg>Daily<br>Intensions</div>
    <div class="tab"><svg><use href="#i-game"/></svg>Gamification</div>
    <div class="tab"><svg><use href="#i-clip"/></svg>Progress<br>Tracking</div>
  </nav>
</section>

<!-- Verbatims: week list -->
<section class="phone" style="left:1285px;height:1085px">
  <header class="phone-head">
    <span class="status">8:41 Am</span><svg class="status-icons" width="64" height="12"><use href="#i-status"/></svg>
    <h1 class="screen-title">Verbatims</h1>
  </header>
  <div class="brand-pill"><span class="brand-dot"></span><span class="brand-name">PathMentor</span></div>

  <div class="seg"><span class="on">Weekly</span><span class="off">Monthly</span></div>
  <div class="week-row" style="top:218px">2025 - Week 22<svg width="14" height="14"><use href="#i-chev"/></svg></div>
  <div class="week-row" style="top:266px">2025 - Week 21<svg width="14" height="14"><use href="#i-chev"/></svg></div>
  <div class="week-row" style="top:314px">2025 - Week 20<svg width="14" height="14"><use href="#i-chev"/></svg></div>
  <div class="week-row" style="top:362px">2025 - Week 19<svg width="14" height="14"><use href="#i-chev"/></svg></div>
  <div class="week-row" style="top:410px">2025 - Week 18<svg width="14" height="14"><use href="#i-chev"/></svg></div>
  <div class="week-row" style="top:458px">2025 - Week 17<svg width="14" height="14"><use href="#i-chev"/></svg></div>
  <div class="week-row" style="top:506px">2025 - Week 16<svg width="14" height="14"><use href="#i-chev"/></svg></div>
  <div class="week-row" style="top:554px">2025 - Week 15<svg width="14" height="14"><use href="#i-chev"/></svg></div>
  <div class="week-row" style="top:602px">2025 - Week 14<svg width="14" height="14"><use href="#i-chev"/></svg></div>
  <div class="week-row" style="top:650px">2025 - Week 13<svg width="14" height="14"><use href="#i-chev"/></svg></div>
  <div class="week-row" style="top:698px">2025 - Week 12<svg width="14" height="14"><use href="#i-chev"/></svg></div>
  <div class="week-row" style="top:746px">2025 - Week 11<svg width="14" height="14"><use href="#i-chev"/></svg></div>
  <div class="week-row" style="top:794px">2025 - Week 10<svg width="14" height="14"><use href="#i-chev"/></svg></div>
  <div class="week-row" style="top:842px">2025 - Week 9<svg width="14" height="14"><use href="#i-chev"/></svg></div>
  <div class="week-row" style="top:890px">2025 - Week 8<svg width="14" height="14"><use href="#i-chev"/></svg></div>
  <div class="week-row" style="top:938px">2025 - Week 7<svg width="14" height="14"><use href="#i-chev"/></svg></div>

  <nav class="tabbar" style="height:67px">
    <div class="tab" style="font-size:9px"><svg><use href="#i-home"/></svg>Home</div>
    <div class="tab active"><span class="disc"><svg style="color:#fff"><use href="#i-chart"/></svg></span>Reports</div>
    <div class="tab" style="font-size:9px"><svg><use href="#i-ask"/></svg>Questions</div>
    <div class="tab" style="font-size:9px"><svg><use href="#i-menu"/></svg>More</div>
  </nav>
</section>

<!-- Verbatims: entries -->
<section class="phone" style="left:1690px;height:941px">
  <header class="phone-head">
    <span class="status">8:41 Am</span><svg class="status-icons" width="64" height="12"><use href="#i-status"/></svg>
    <h1 class="screen-title">Verbatims</h1>
  </header>
  <div class="brand-pill"><span class="brand-dot"></span><span class="brand-name">PathMentor</span></div>

  <article class="vcard" style="top:153px;height:163px">
    <div class="vcard-head">Week 22- 2025</div>
    <div class="entry"><b>27 May 2025</b><svg class="bell" width="16" height="16"><use href="#i-bell"/></svg><br>lichaam beter, bol kans, joris hulp meisje<br>potloden<br><span class="btn-report">Show Report</span></div>
  </article>
  <article class="vcard" style="top:325px;height:143px">
    <div class="vcard-head">Week 21 - 2025</div>
    <div class="entry"><b>19 May 2025</b><svg class="bell" width="16" height="16"><use href="#i-bell"/></svg><br>weer, mats<br><span class="btn-report">Show Report</span></div>
  </article>
  <article class="vcard" style="top:479px;height:361px">
    <div class="vcard-head">Week 20 - 2025</div>
    <div class="entry"><b>15 May 2025</b><svg class="bell" width="16" height="16"><use href="#i-bell"/></svg><br>hvf<br>bol, marijke</div>
    <div class="entry"><b>14 May 2025</b><svg class="bell" width="16" height="16"><use href="#i-bell"/></svg><br>Klanten, sport, Tijs<br>Marijke, Liesel</div>
    <div class="entry"><b>13 May 2025</b><svg class="bell" width="16" height="16"><use href="#i-bell"/></svg><br>bol, ben Vermaat, weer<br>bol,<br><span class="btn-report">Show Report</span></div>
  </article>

  <nav class="tabbar" style="height:67px">
    <div class="tab" style="font-size:9px"><svg><use href="#i-home"/></svg>Home</div>
    <div class="tab active"><span class="disc"><svg style="color:#fff"><use href="#i-chart"/></svg></span>Reports</div>
    <div class="tab" style="font-size:9px"><svg><use href="#i-ask"/></svg>Questions</div>
    <div class="tab" style="font-size:9px"><svg><use href="#i-menu"/></svg>More</div>
  </nav>
</section>

<!-- Gamification -->
<section class="phone" style="left:2095px;height:1361px">
  <header class="phone-head">
    <span class="status">8:41 Am</span><svg class="status-icons" width="64" height="12"><use href="#i-status"/></svg>
    <h1 class="screen-title">Gamification</h1>
  </header>
  <div class="brand-pill"><span class="brand-dot"></span><span class="brand-name">PathMentor</span></div>

  <p class="section" style="top:152px"><svg width="12" height="14"><path d="M6 1c1 4 5 5 5 9a5 5 0 0 1-10 0c0-2 1-3 2-4 0 2 1 3 2 3 0-3-1-5 1-8z" fill="#F26B1D"/></svg>Daily Streak Tracker</p>
  <div class="card" style="left:16px;top:186px;width:301px;height:217px;box-shadow:none;border:1px solid var(--line)">
    <div class="streak-art" role="img" aria-label="Four seedlings in soil, growing larger from left to right to show the streak"></div>
    <p class="abs" style="left:18px;top:130px;font-size:13px;line-height:1.85">You’ve shown up <b>4 days</b> in a row<br>– keep it going!</p>
    <p class="abs" style="left:18px;top:184px;font-size:13px;color:#bbb;white-space:nowrap">You’ve made this a habit - <b style="color:#111;font-weight:800">INCREDIBLE!</b></p>
  </div>

  <p class="section" style="top:416px"><svg width="14" height="14"><circle cx="7" cy="6" r="5" fill="#F59B1D"/><path d="M4 10 3 14l4-2 4 2-1-4" fill="#F26B1D"/></svg>Milestone Rewards</p>
  <div class="card" style="left:16px;top:449px;width:301px;height:479px;box-shadow:none;border:1px solid var(--line)">
    <p class="abs" style="left:18px;top:12px;font-size:13.5px;line-height:1.8">Celebratory moments at 3, 7, 14, 30<br>days, etc</p>
    <svg class="abs" style="left:37px;top:120px" width="2" height="250"><line x1="1" y1="0" x2="1" y2="250" stroke="#bbb" stroke-dasharray="3 3"/></svg>
    <div class="badge" style="top:77px"><span class="medal"><svg width="20" height="20"><circle cx="10" cy="9" r="5" fill="#222"/><rect x="8" y="15" width="4" height="3" fill="#222"/></svg></span><div><p class="name">Intentional 7</p><p class="meta"><svg width="10" height="10"><use href="#i-lock"/></svg>Unlocked <small>06 May 2025</small></p></div></div>
    <div class="badge" style="top:143px"><span class="medal"><svg width="20" height="20"><circle cx="10" cy="10" r="6" fill="#222"/></svg></span><div><p class="name">Mindful Explorer</p><p class="meta"><svg width="10" height="10"><use href="#i-lock"/></svg>Unlocked <small>06 May 2025</small></p></div></div>
    <div class="badge" style="top:208px"><span class="medal"><svg width="20" height="20"><rect x="5" y="3" width="10" height="14" rx="2" fill="#222"/></svg></span><div><p class="name">Seeker</p><p class="meta"><svg width="10" height="10"><use href="#i-lock"/></svg>Unlocked <small>06 May 2025</small></p></div></div>
    <div class="badge faded" style="top:279px"><span class="medal"><svg width="20" height="20"><circle cx="10" cy="9" r="5" fill="#222"/></svg></span><div><p class="name">Intentional 7</p><p class="meta"><svg width="10" height="10"><use href="#i-lock"/></svg>Unlocked <small>06 May 2025</small></p></div></div>
    <div class="badge faded" style="top:345px"><span class="medal"><svg width="20" height="20"><circle cx="10" cy="10" r="6" fill="#222"/></svg></span><div><p class="name">Mindful Explorer</p><p class="meta"><svg width="10" height="10"><use href="#i-lock"/></svg>Unlocked <small>06 May 2025</small></p></div></div>
    <span class="abs" style="left:18px;top:401px;background:var(--yellow);border-radius:16px;font-size:13.5px;font-weight:600;padding:5px 14px">Load More Rewards</span>
    <p class="abs" style="left:18px;top:443px;font-size:13.5px;color:#aaa">Next reward unlocks in <b style="color:#111">3 days!</b></p>
  </div>

  <p class="section" style="top:944px"><svg width="14" height="14"><rect x="1" y="3" width="12" height="10" rx="1" fill="#F5B400"/></svg>Levels / XP System</p>
  <div class="xp-row" style="top:978px">Setting intentions<svg width="20" height="20" style="color:#777"><use href="#i-chart"/></svg></div>
  <div class="xp-row" style="top:1034px">Completing reflections<svg width="18" height="18"><circle cx="9" cy="9" r="8" fill="#777"/><path d="m5 9 3 3 5-6" stroke="#fff" stroke-width="1.8" fill="none"/></svg></div>
  <div class="xp-row" style="top:1090px">Providing feedback or journaling<svg width="20" height="20" style="color:#777"><use href="#i-ask"/></svg></div>

  <p class="abs" style="left:15px;top:1149px;font-size:16px">Our Progress</p>
  <svg class="abs" style="left:0;top:1184px" width="333" height="30">
    <line x1="30" y1="14" x2="50" y2="14" stroke="var(--cream)" stroke-width="3"/>
    <line x1="50" y1="14" x2="155" y2="14" stroke="var(--yellow)" stroke-width="3"/>
    <line x1="155" y1="14" x2="295" y2="14" stroke="#D5D5D5" stroke-width="3"/>
    <circle cx="50" cy="14" r="12" fill="var(--yellow)"/><path d="m44 14 4 4 8-8" stroke="#111" stroke-width="2" fill="none"/>
    <circle cx="155" cy="14" r="12" fill="var(--yellow)"/><path d="m149 14 4 4 8-8" stroke="#111" stroke-width="2" fill="none"/>
    <circle cx="257" cy="14" r="12" fill="#C9C9C9"/><path d="m251 14 4 4 8-8" stroke="#fff" stroke-width="2" fill="none"/>
  </svg>
  <p class="level" style="left:1px"><b style="font-weight:600">Level 01</b><br>Basic Details</p>
  <p class="level" style="left:108px"><b style="font-weight:600">Level 02</b><br>Clarity Seeker</p>
  <p class="level" style="left:207px"><b style="font-weight:600">Next</b><br>at 500 XP</p>

  <nav class="tabbar" style="height:66px">
    <div class="tab" style="font-size:9px"><svg><use href="#i-home"/></svg>Home</div>
    <div class="tab active"><span class="disc"><svg style="color:#fff"><use href="#i-chart"/></svg></span>Reports</div>
    <div class="tab" style="font-size:9px"><svg><use href="#i-ask"/></svg>Questions</div>
    <div class="tab" style="font-size:9px"><svg><use href="#i-menu"/></svg>More</div>
  </nav>
</section>

</main>
</body>
</html>
```